Jewelry Shop Needs a Business Card Design

***We want a very sharp and unforgettable pantone for the Business Card. ***
***We do not want the business card or logo only in black, white and grey color!!!Please provide us a main color as our brand topic! Thanks!! ***

Mabel’s Nook is a Hong Kong based fine jewelry brand.

We want a very nice, simple and elegant business card design for Mabel's Nook Brand. The company's logo has been uploaded already.

You can design with below info:

Dorian Fung
Director
M: +852 94273658
T: +852 35820417
F: +852 35820419
E: dorian.fung@mabelsnook.example
5/F , Harbourlight Tower, 12-18 Orchid Lane, Wan Tung Kok, Kowloon, Hong Kong

Target Market(s)

Mabel’s Nook philosophy is a jewelry icon of young, creative, trendy, fashionable, stylish, energetic, and elegant. For Mabel’s Nook, jewelry is one collection of artworks, the most important items in personal life.

Industry/Entity Type

Jewelry

Requirements
Must have
• We want a very sharp and unforgettable pantone for the Business Card.

```html
<!DOCTYPE html>
<html lang="en">
<head>
<meta charset="utf-8">
<title>Mabel’s Nook – Business Card</title>
<link rel="stylesheet" href="https://fonts.googleapis.com/css2?family=Open+Sans:wght@400;700&display=swap">
<style>
  :root {
    --backdrop: #e4e4e4;
    --cream: #efe9dc;
    --cream-deep: #e3dac6;
    --gold: #c9a441;
    --gold-light: #e6c75e;
    --bronze: #85591f;
    --ink-light: #f4e9d6;
    --ink-soft: #e6cfa8;
    --white: #ffffff;
  }
  * { box-sizing: border-box; margin: 0; padding: 0; }
  html, body { width: 1200px; height: 1200px; overflow: hidden; }
  body {
    background: var(--backdrop);
    font-family: "Open Sans", Arial, sans-serif;
    display: flex;
    flex-direction: column;
    align-items: center;
    justify-content: center;
    gap: 80px;
  }
  .card {
    position: relative;
    width: 760px;
    height: 434px;
    overflow: hidden;
    box-shadow: 0 10px 30px rgba(0,0,0,0.12);
  }

  /* Front */
  .card-front { background: var(--cream); }
  .front-texture {
    position: absolute; inset: 0;
    background: radial-gradient(circle at 50% 50%, var(--cream) 0%, var(--cream-deep) 100%);
  }
  .front-frame {
    position: absolute; inset: 34px;
    border: 2px solid var(--gold);
  }
  .front-frame::after {
    content: ""; position: absolute; inset: 6px;
    border: 1px solid var(--gold);
  }
  .front-brand {
    position: absolute; inset: 0;
    display: flex; flex-direction: column; align-items: center; justify-content: center;
    gap: 18px;
  }
  .brand-dot {
    width: 120px; height: 120px; border-radius: 50%;
    background: var(--gold);
  }
  .brand-name {
    font-family: "Open Sans", Arial, sans-serif;
    font-weight: 400;
    font-size: 26px;
    color: var(--bronze);
  }

  /* Back */
  .card-back { background: var(--bronze); color: var(--ink-light); }
  .accent-bar {
    position: absolute; left: 44px; width: 12px;
    background: var(--gold-light);
  }
  .accent-top { top: 30px; height: 44px; }
  .accent-bottom { top: 330px; height: 30px; }
  .contact-block { position: absolute; left: 96px; top: 56px; }
  .person-name { font-weight: 700; font-size: 28px; line-height: 1.1; }
  .person-role { font-size: 15px; color: var(--ink-soft); margin-bottom: 16px; }
  .address { font-size: 18px; line-height: 1.3; padding-left: 24px; margin-bottom: 16px; }
  .contact-list { list-style: none; font-size: 18px; line-height: 1.35; }
  .contact-list li { display: flex; align-items: center; gap: 12px; }
  .contact-icon { width: 16px; height: 16px; flex: none; }
  .back-brand {
    position: absolute; right: 60px; bottom: 50px;
    display: flex; flex-direction: column; align-items: center; gap: 10px;
  }
  .back-brand .brand-dot { width: 76px; height: 76px; background: var(--white); }
  .back-brand .brand-name { font-size: 16px; color: var(--white); }
</style>
</head>
<body>

<section class="card card-front">
  <div class="front-texture" role="img" aria-label="Soft cream pattern of overlapping circles"></div>
  <div class="front-frame"></div>
  <div class="front-brand">
    <div class="brand-dot"></div>
    <div class="brand-name">Mabel’s Nook</div>
  </div>
</section>

<section class="card card-back">
  <div class="accent-bar accent-top"></div>
  <div class="accent-bar accent-bottom"></div>
  <div class="contact-block">
    <h1 class="person-name">Dorian Fung</h1>
    <p class="person-role">Director</p>
    <p class="address">5/F , Harbourlight Tower,<br>12-18 Orchid Lane, Wan Tung Kok,<br>Kowloon, Hong Kong</p>
    <ul class="contact-list">
      <li>
        <svg class="contact-icon" viewBox="0 0 16 16"><rect width="16" height="16" rx="3" fill="#e6c75e"/><rect x="5" y="3" width="6" height="10" rx="1" fill="none" stroke="#85591f" stroke-width="1.4"/></svg>
        +852 94273658
      </li>
      <li>
        <svg class="contact-icon" viewBox="0 0 16 16"><rect width="16" height="16" rx="3" fill="#e6c75e"/><path d="M4 5c0 4 3 7 7 7l1-2-2-1-1 1c-1-.5-2-1.5-2.5-2.5l1-1-1-2z" fill="#85591f"/></svg>
        +852 35820417
      </li>
      <li>
        <svg class="contact-icon" viewBox="0 0 16 16"><rect width="16" height="16" rx="3" fill="#e6c75e"/><rect x="3" y="6" width="10" height="6" fill="#85591f"/><rect x="5" y="3" width="6" height="4" fill="none" stroke="#85591f" stroke-width="1.2"/></svg>
        +852 35820419
      </li>
      <li>
        <svg class="contact-icon" viewBox="0 0 16 16"><rect width="16" height="16" rx="3" fill="#e6c75e"/><rect x="3" y="4.5" width="10" height="7" fill="none" stroke="#85591f" stroke-width="1.2"/><path d="M3 4.5l5 4 5-4" fill="none" stroke="#85591f" stroke-width="1.2"/></svg>
        dorian.fung@mabelsnook.example
      </li>
    </ul>
  </div>
  <div class="back-brand">
    <div class="brand-dot"></div>
    <div class="brand-name">Mabel’s Nook</div>
  </div>
</section>

</body>
</html>
```